Mobile App UI Redesign for Service Booking app

Bookora is a business management system made especially for service based businesses (our subscribers). It enables systemising your service businesses. This can be used by diverse industries like automotive service, beauty (hair salons, nail spas), Spas, Chiropractor, acupuntcure, osteo, yoga studio, business coach, etc.

One component of this management system is a consumer app that the users (customers of our subscribers) can use to book in services with businesses (subscribers). Any business that provides services, either 1-to-1(personal training/ hair cut, etc) or 1-to-many (classes/ sessions)can get their users to download the app and book straight away in real time.

The current app is built as a version that is available to all subscribers. Hence the search screen at the beginning of the app. Our subscribers have the option to brand this app, with their own logo and colours.

The UI of the app needs to be designed using flat and clean UI design trends that are currently prevailing for B2C apps. Even the sliding menu panel can be removed and alternative placement of this functionality can be suggested. The color palette used for the design should be limited (3-5 colours) so that minimum effort is required to convert this into our customers branded app.

The Current UI screens are open to suggestions for change. For ease of booking in minimum steps, consolidation of functionality on different screens can be suggested, accompanies by a rational reason with the objective of having a simple and straight forward user experience.

User should be able to move from one function to another (booking > view appointments > profile) in no more than 1 or max 2 gestures.

Target Market(s)

Service Based Businesses that require customers to book in services or sessions with them. These can include health services (chiro, physio, osteo, accupuncture, etc) Beauty (hair salon, nail spa, health spa, etc) automotive service (car service, motorcycle service, bike service, etc)

Industry/Entity Type

Business

Requirements
Must have
• Design files to be delivered in JPG and Vectored PSD format

```html
<!DOCTYPE html>
<html lang="en">
<head>
<meta charset="utf-8">
<title>Bookora – App Screens</title>
<link href="https://fonts.googleapis.com/css2?family=Open+Sans:wght@400;600;700&display=swap" rel="stylesheet">
<style>
:root{
  --bg:#e9eaec;
  --screen:#ffffff;
  --brand:#35a7e0;
  --brand-dark:#1f8cc4;
  --accent:#f7931e;
  --ink:#333a40;
  --muted:#7b8288;
  --line:#dcdfe2;
  --panel:#eef0f2;
  --field:#ffffff;
  --status:#f5f5f5;
  --red:#d9232e;
  --green:#1e7a4f;
}
*{box-sizing:border-box;margin:0;padding:0}
html,body{width:1200px;height:2368px;overflow:hidden;background:var(--bg);font-family:"Open Sans",Arial,sans-serif;color:var(--ink)}
.board{position:relative;width:1200px;height:2368px}
.screen{position:absolute;width:480px;height:852px;background:var(--screen);overflow:hidden;box-shadow:0 6px 24px rgba(0,0,0,.12)}
.s1{left:80px;top:240px}.s2{left:640px;top:240px}.s3{left:80px;top:1292px}.s4{left:640px;top:1292px}
.status{height:30px;background:var(--status);display:flex;align-items:center;justify-content:space-between;padding:0 12px;font-size:13px;font-weight:600;color:#222}
.navbar{height:60px;background:var(--brand);display:flex;align-items:center;justify-content:center;position:relative;color:#fff;font-size:15px;font-weight:600;letter-spacing:.5px;text-transform:uppercase}
.navbar .left,.navbar .right{position:absolute;top:0;height:60px;width:60px;display:flex;align-items:center;justify-content:center}
.navbar .left{left:0}.navbar .right{right:0}
.navbar .left.active{background:var(--brand-dark)}
.intro{padding:42px 48px 30px;text-align:center;font-size:17px;line-height:1.55;color:var(--ink)}
.search-panel{margin:0 24px;background:var(--panel);padding:24px 18px;display:flex;flex-direction:column;gap:14px}
.field{height:46px;background:var(--field);border:1px solid var(--line);border-radius:3px;display:flex;align-items:center;justify-content:space-between;padding:0 14px;font-size:14px;color:#a3a8ad}
.caret{width:0;height:0;border-left:6px solid transparent;border-right:6px solid transparent;border-top:7px solid #8a9095}
.btn{height:52px;background:var(--accent);color:#fff;border-radius:4px;display:flex;align-items:center;justify-content:center;gap:10px;font-size:17px;font-weight:700;text-transform:uppercase}
.detail{padding:30px 36px 0;text-align:center}
.detail h1{font-size:26px;font-weight:600;margin-bottom:16px}
.brand-mark{width:116px;height:116px;border-radius:50%;background:var(--red);margin:0 auto 18px}
.city{font-size:16px;font-weight:700;text-transform:uppercase}
.addr{font-size:15px;line-height:1.45;color:var(--ink)}
.phone{display:inline-flex;align-items:center;gap:8px;font-size:15px;margin-top:4px}
.about{text-align:left;font-size:13.5px;line-height:1.55;color:var(--muted);margin:26px 0 16px}
.fav-toggle{display:flex;align-items:center;gap:10px;font-size:14px;color:var(--brand);margin-bottom:16px}
.fav-toggle .box{width:16px;height:16px;border:2px solid var(--brand);border-radius:2px}
.search-bar{height:66px;background:var(--panel);padding:12px 14px;border-bottom:1px solid var(--line)}
.search-bar .field{height:42px;color:#a3a8ad}
.listing{display:flex;gap:18px;padding:22px 18px;border-bottom:1px solid var(--line)}
.thumb{flex:none;width:84px;height:84px}
.thumb.red{background:var(--red)}
.thumb.round{display:flex;align-items:center;justify-content:center}
.thumb.round span{width:80px;height:80px;border-radius:50%;background:var(--green)}
.listing .name{font-size:17px;font-weight:700;color:var(--accent);margin-bottom:2px}
.listing .city{font-size:14px}
.listing .addr{font-size:13.5px;line-height:1.45}
.listing .phone{font-size:13.5px}
</style>
</head>
<body>
<main class="board">

  <!-- Search screen -->
  <section class="screen s1">
    <div class="status"><span>Carrier</span><span>1:20PM</span><span>100%</span></div>
    <header class="navbar">Search
      <span class="right"><svg width="22" height="16" viewBox="0 0 22 16"><rect width="22" height="2.6" fill="#fff"/><rect y="6.7" width="22" height="2.6" fill="#fff"/><rect y="13.4" width="22" height="2.6" fill="#fff"/></svg></span>
    </header>
    <p class="intro">Search here for businesses that are trialling Bookora app to provide you with convenience of booking their services on your mobile!</p>
    <div class="search-panel">
      <div class="field">Search business by name...</div>
      <div class="field">Select city...<span class="caret"></span></div>
      <div class="field">Select business type...<span class="caret"></span></div>
      <div class="field">Select postal code...<span class="caret"></span></div>
      <div class="btn"><svg width="20" height="20" viewBox="0 0 20 20"><circle cx="8" cy="8" r="6" fill="none" stroke="#fff" stroke-width="2.6"/><line x1="12.5" y1="12.5" x2="18" y2="18" stroke="#fff" stroke-width="3" stroke-linecap="round"/></svg>Search</div>
    </div>
  </section>

  <!-- Business detail screen -->
  <section class="screen s2">
    <div class="status"><span>Carrier</span><span>1:20PM</span><span>100%</span></div>
    <header class="navbar">Move Well Physio
      <span class="left"><svg width="12" height="20" viewBox="0 0 12 20"><polyline points="10,2 2,10 10,18" fill="none" stroke="#fff" stroke-width="2.6"/></svg></span>
      <span class="right"><svg width="22" height="16" viewBox="0 0 22 16"><rect width="22" height="2.6" fill="#fff"/><rect y="6.7" width="22" height="2.6" fill="#fff"/><rect y="13.4" width="22" height="2.6" fill="#fff"/></svg></span>
    </header>
    <div class="detail">
      <h1>Move Well Physio</h1>
      <div class="brand-mark" role="img" aria-label="Business logo area"></div>
      <div class="city">Melbourne / 3000</div>
      <div class="addr">Level 2, 18 Harbour Lane<br>Eastvale VIC 3190</div>
      <div class="phone"><svg width="18" height="18" viewBox="0 0 18 18"><circle cx="9" cy="9" r="8" fill="none" stroke="#333a40" stroke-width="1.5"/><path d="M6 5l1.6-.4 1 2.2-1 .8c.5 1.2 1.3 2 2.5 2.6l.8-1 2.2 1-.4 1.6c-3.3.2-6.8-3.4-6.7-6.8z" fill="#333a40"/></svg>1300 555 210</div>
      <p class="about">Hands-on physiotherapy, remedial massage and movement coaching for all ages. Book a session in seconds, choose your preferred practitioner and time, and get reminders before every visit. Our friendly team helps you recover faster and stay active all year round.</p>
      <div class="fav-toggle"><span class="box"></span>Remove from favourites</div>
      <div class="btn"><svg width="20" height="20" viewBox="0 0 20 20"><path d="M1 9l18-8-7 18-3-7z" fill="#fff"/></svg>Select Business</div>
    </div>
  </section>

  <!-- Favourites list -->
  <section class="screen s3">
    <div class="status"><span>Carrier</span><span>1:20PM</span><span>100%</span></div>
    <header class="navbar">Favourites
      <span class="left"><svg width="20" height="20" viewBox="0 0 20 20"><circle cx="8" cy="8" r="6" fill="none" stroke="#fff" stroke-width="2.4"/><line x1="12.5" y1="12.5" x2="18" y2="18" stroke="#fff" stroke-width="2.8" stroke-linecap="round"/></svg></span>
      <span class="right"><svg width="22" height="16" viewBox="0 0 22 16"><rect width="22" height="2.6" fill="#fff"/><rect y="6.7" width="22" height="2.6" fill="#fff"/><rect y="13.4" width="22" height="2.6" fill="#fff"/></svg></span>
    </header>
    <article class="listing">
      <div class="thumb red" role="img" aria-label="Move Well Physio logo area"></div>
      <div>
        <div class="name">Move Well Physio</div>
        <div class="city">Melbourne / 3000</div>
        <div class="addr">Level 2, 18 Harbour Lane<br>Eastvale VIC 3190</div>
        <div class="phone"><svg width="16" height="16" viewBox="0 0 18 18"><circle cx="9" cy="9" r="8" fill="none" stroke="#333a40" stroke-width="1.5"/><path d="M6 5l1.6-.4 1 2.2-1 .8c.5 1.2 1.3 2 2.5 2.6l.8-1 2.2 1-.4 1.6c-3.3.2-6.8-3.4-6.7-6.8z" fill="#333a40"/></svg>1300 555 210</div>
      </div>
    </article>
    <article class="listing">
      <div class="thumb round" role="img" aria-label="Bean Corner logo area"><span></span></div>
      <div>
        <div class="name">Bean Corner</div>
        <div class="city">Sydney / 2000</div>
        <div class="addr">14 Quay Street<br>Sydney NSW 2000</div>
        <div class="phone"><svg width="16" height="16" viewBox="0 0 18 18"><circle cx="9" cy="9" r="8" fill="none" stroke="#333a40" stroke-width="1.5"/><path d="M6 5l1.6-.4 1 2.2-1 .8c.5 1.2 1.3 2 2.5 2.6l.8-1 2.2 1-.4 1.6c-3.3.2-6.8-3.4-6.7-6.8z" fill="#333a40"/></svg>02 5550 1847</div>
      </div>
    </article>
  </section>

  <!-- Favourites with search open -->
  <section class="screen s4">
    <div class="status"><span>Carrier</span><span>1:20PM</span><span>100%</span></div>
    <header class="navbar">Favourites
      <span class="left active"><svg width="20" height="20" viewBox="0 0 20 20"><circle cx="8" cy="8" r="6" fill="none" stroke="#fff" stroke-width="2.4"/><line x1="12.5" y1="12.5" x2="18" y2="18" stroke="#fff" stroke-width="2.8" stroke-linecap="round"/></svg></span>
      <span class="right"><svg width="22" height="16" viewBox="0 0 22 16"><rect width="22" height="2.6" fill="#fff"/><rect y="6.7" width="22" height="2.6" fill="#fff"/><rect y="13.4" width="22" height="2.6" fill="#fff"/></svg></span>
    </header>
    <div class="search-bar">
      <div class="field">Search business by name...<svg width="18" height="18" viewBox="0 0 20 20"><circle cx="8" cy="8" r="6" fill="none" stroke="#8a9095" stroke-width="2.4"/><line x1="12.5" y1="12.5" x2="18" y2="18" stroke="#8a9095" stroke-width="2.8" stroke-linecap="round"/></svg></div>
    </div>
    <article class="listing">
      <div class="thumb red" role="img" aria-label="Move Well Physio logo area"></div>
      <div>
        <div class="name">Move Well Physio</div>
        <div class="city">Melbourne / 3000</div>
        <div class="addr">Level 2, 18 Harbour Lane<br>Eastvale VIC 3190</div>
        <div class="phone"><svg width="16" height="16" viewBox="0 0 18 18"><circle cx="9" cy="9" r="8" fill="none" stroke="#333a40" stroke-width="1.5"/><path d="M6 5l1.6-.4 1 2.2-1 .8c.5 1.2 1.3 2 2.5 2.6l.8-1 2.2 1-.4 1.6c-3.3.2-6.8-3.4-6.7-6.8z" fill="#333a40"/></svg>1300 555 210</div>
      </div>
    </article>
    <article class="listing">
      <div class="thumb round" role="img" aria-label="Bean Corner logo area"><span></span></div>
      <div>
        <div class="name">Bean Corner</div>
        <div class="city">Sydney / 2000</div>
        <div class="addr">14 Quay Street<br>Sydney NSW 2000</div>
        <div class="phone"><svg width="16" height="16" viewBox="0 0 18 18"><circle cx="9" cy="9" r="8" fill="none" stroke="#333a40" stroke-width="1.5"/><path d="M6 5l1.6-.4 1 2.2-1 .8c.5 1.2 1.3 2 2.5 2.6l.8-1 2.2 1-.4 1.6c-3.3.2-6.8-3.4-6.7-6.8z" fill="#333a40"/></svg>02 5550 1847</div>
      </div>
    </article>
  </section>

</main>
</body>
</html>
```